Cat-products company needs smart, yet endearing, business card

We need a business card design for a new, but up-and-running, business based in Honolulu, Hawaii. The business is Purrlane Nest Co. Our first product is the most environmentally-friendly cat grass kit ever seen on the planet. Future products, currently in the R&D phase, will include a variety of exciting cat scratchers. We also do consulting work to help apartment-dwellers make their home more cat-friendly and, in the future, plan on doing full, custom installs of structure to create high walkways for cats.

Target Market(s)

Middle-aged, apartment-dwelling, middle-class workers who own 1 or more cats and who dote on them.

Industry/Entity Type

Pet Care

Contact Information for Business Card

A striking, professional, yet warm and friendly design is what we're after.

Font styles to use
Serif
Sans Serif
Other font styles liked:
• Comfortaa

Colors

Designer to choose colors to be used in the design.

Requirements
Must have
• The company logo: (see attachment)
• The company name: Purrlane Nest Co
• The web address: www.purrlanenestco.example
• Email: support@purrlanenestco.example
• Phone: +1 (808) 555 0172
• Update (Fri Jun 30 3017 7:45pm Hawaii Time) I would like, is possible, uploaded picture of the cat grass kit on the back of the card with some text along the lines of: Purrlane Nest Co - Where The Freshest Kitty Sprouts Begin
Nice to have
• A cat picture, cartoon, real or silhouette that illustrates cats in action and/or relaxing; ie using the apartment space to live, play and relax in and being well-contented.
• Most of the website is done in the font: Comfortaa. It might be nice to continue using this for brand consistency.
Should not have
• Hard-to-read fonts.

```html
<!DOCTYPE html>
<html lang="en">
<head>
<meta charset="utf-8">
<title>Purrlane Nest Co — Business Card</title>
<link rel="stylesheet" href="https://fonts.googleapis.com/css2?family=Fredoka:wght@600&family=Comfortaa:wght@400;700&display=swap">
<style>
  :root {
    --brown: #55332c;
    --gold: #f7b217;
    --white: #ffffff;
    --stage: #2a2a2a;
    --photo-a: #d9d4cc;
    --photo-b: #b9874f;
  }
  * { box-sizing: border-box; margin: 0; padding: 0; }
  html, body { width: 1200px; height: 1076px; overflow: hidden; }
  body {
    background: var(--stage);
    display: flex; flex-direction: column; align-items: center; justify-content: center;
    gap: 40px;
    font-family: "Comfortaa", sans-serif;
  }
  .card {
    width: 880px; height: 480px;
    background: var(--white);
    position: relative; overflow: hidden;
    box-shadow: 0 10px 30px rgba(0,0,0,.5);
  }
  .wordmark {
    font-family: "Fredoka", sans-serif; font-weight: 600;
    color: var(--gold); line-height: 1.02; text-align: center;
  }
  /* front */
  .front .wordmark { position: absolute; left: 70px; top: 150px; width: 320px; font-size: 52px; }
  .front .divider { position: absolute; left: 420px; top: 90px; width: 2px; height: 170px; background: var(--brown); }
  .details { position: absolute; left: 480px; top: 110px; color: var(--brown); }
  .name { font-size: 26px; font-weight: 700; color: var(--gold); }
  .name span { color: var(--brown); }
  .role { font-size: 16px; margin-top: 2px; }
  .contact { list-style: none; margin-top: 48px; font-size: 18px; }
  .contact li { display: flex; align-items: center; gap: 10px; margin-bottom: 8px; }
  .contact .dot { width: 22px; height: 22px; border-radius: 50%; background: var(--brown); display: flex; align-items: center; justify-content: center; }
  .web-band {
    position: absolute; left: 0; right: 0; bottom: 55px; height: 62px;
    background: var(--brown); color: var(--gold);
    font-size: 22px; font-weight: 700; letter-spacing: 3px;
    display: flex; align-items: center; padding-left: 160px;
  }
  .band-square { position: absolute; right: 100px; bottom: 40px; width: 92px; height: 92px; background: var(--white); display:flex; align-items:center; justify-content:center; }
  .band-square i { width: 64px; height: 64px; background: var(--brown); display:block; }
  /* back */
  .photo {
    position: absolute; left: 0; top: 0; width: 470px; height: 100%;
    background: linear-gradient(160deg, var(--photo-a) 0%, #ece8e1 45%, var(--photo-b) 100%);
  }
  .back .brand { position: absolute; left: 520px; top: 120px; width: 320px; display: flex; flex-direction: column; align-items: center; gap: 18px; }
  .back .mark-square { width: 70px; height: 70px; background: var(--brown); }
  .back .wordmark { font-size: 54px; }
  .social { display: flex; gap: 22px; margin-top: 14px; }
  .social li { list-style: none; width: 48px; height: 48px; background: var(--brown); border-radius: 4px; }
</style>
</head>
<body>
  <section class="card front" aria-label="Card front">
    <div class="wordmark">Purrlane<br>Nest Co</div>
    <div class="divider"></div>
    <div class="details">
      <p class="name">Employee <span>Name</span></p>
      <p class="role">Manager</p>
      <ul class="contact">
        <li><span class="dot"><svg width="12" height="12" viewBox="0 0 24 24"><path fill="#f7b217" d="M6.6 10.8a15 15 0 0 0 6.6 6.6l2.2-2.2a1 1 0 0 1 1-.25 11 11 0 0 0 3.6.6 1 1 0 0 1 1 1V20a1 1 0 0 1-1 1A17 17 0 0 1 3 4a1 1 0 0 1 1-1h3.5a1 1 0 0 1 1 1 11 11 0 0 0 .6 3.6 1 1 0 0 1-.25 1z"/></svg></span>+1 (808) 555 0172</li>
        <li><span class="dot"><svg width="12" height="10" viewBox="0 0 24 18"><rect x="1" y="1" width="22" height="16" fill="#f7b217"/><path d="M1 1l11 9 11-9" fill="none" stroke="#55332c" stroke-width="2"/></svg></span>support@purrlanenestco.example</li>
      </ul>
    </div>
    <div class="web-band">www.purrlanenestco.example</div>
    <div class="band-square"><i></i></div>
  </section>

  <section class="card back" aria-label="Card back">
    <div class="photo" role="img" aria-label="Photo of cats climbing wall shelves and stretching up a sisal scratching post indoors"></div>
    <div class="brand">
      <div class="mark-square"></div>
      <div class="wordmark">Purrlane<br>Nest Co</div>
      <ul class="social" aria-label="Social media">
        <li></li><li></li><li></li><li></li>
      </ul>
    </div>
  </section>
</body>
</html>
```